www.morvalpastime.com

Updating website so looks futristic but yet business like and easy to navigate, essentially a good landing page with a cool picture summing up what we do, and links to the following pages, all other pages on site to be updated, Exclusive Distributor of Brisk Rig Unique Fitness Equipment Products in UK & Ireland, www.ridgesurge.co.uk Exclusive Partners & Distributors Of Ridge Surge - Obstacle Races - Obstacle Hire - Obstacle Training - Adventure Events, www.trekvaliant.co.uk Adventures That Inspire. We also Health Club / Facillity Consultancy

```html
<!DOCTYPE html>
<html lang="en">
<head>
<meta charset="utf-8">
<title>Morval Pastime – Health, Wellness &amp; Fitness Consultants</title>
<link rel="stylesheet" href="https://fonts.googleapis.com/css2?family=Lato:wght@400;700;900&family=Open+Sans:wght@400;600;700&display=swap">
<style>
:root{
  --ink:#1c1c1c;
  --text:#555;
  --muted:#888;
  --brand-red:#c4161c;
  --white:#fff;
  --grey-bg:#efefef;
  --line:#d6d6d6;
  --dark:#2e2e2e;
  --footer:#333;
  --hero-a:#3a3a3c;
  --hero-b:#6d6a68;
  --gym-a:#16324f;
  --gym-b:#6f7f8e;
}
*{box-sizing:border-box;margin:0;padding:0}
html,body{width:1200px;height:4444px;overflow:hidden}
body{font-family:"Open Sans",Arial,sans-serif;color:var(--text);background:var(--white);position:relative}
section,header,footer{position:absolute;left:0;width:1200px}
.abs{position:absolute}

/* nav */
.site-nav{top:0;height:66px;background:var(--white);border-bottom:1px solid #e6e6e6}
.brand{left:98px;top:10px}
.brand-name{font-family:"Lato",sans-serif;font-weight:900;font-size:27px;color:var(--ink);letter-spacing:-.5px;line-height:1}
.brand-tag{font-size:9px;color:var(--brand-red);font-weight:600;margin-top:3px}
.menu{right:38px;top:22px;display:flex;gap:34px;list-style:none;font-size:15px;color:#555}

/* hero */
.hero{top:66px;height:527px;background:linear-gradient(120deg,var(--hero-a),var(--hero-b) 55%,#2b2b2d)}
.hero-title{left:113px;top:180px;font-family:"Lato",sans-serif;font-weight:900;font-size:30px;color:var(--white);letter-spacing:1px;background:rgba(0,0,0,.35);padding:4px 6px}
.hero-sub{left:113px;top:240px;font-family:"Lato",sans-serif;font-weight:700;font-size:15px;color:var(--white);letter-spacing:1px}
.btn-dark{display:inline-block;background:#111;color:var(--white);font-family:"Lato",sans-serif;font-weight:700;font-size:12px;letter-spacing:1.5px;text-transform:uppercase;padding:13px 20px}
.hero .btn-dark{left:113px;top:305px}
.polaroid{background:var(--white);padding:12px 12px 40px;box-shadow:0 6px 18px rgba(0,0,0,.35)}
.polaroid div{width:100%;height:100%}

/* services */
.services{top:593px;height:405px;background:var(--white)}
.service{width:280px;text-align:center;top:65px}
.service .icon{width:172px;height:172px;border-radius:50%;margin:0 auto 44px}
.service h3{font-family:"Lato",sans-serif;font-weight:700;font-size:22px;color:var(--ink);margin-bottom:14px}
.service p{font-size:16px;line-height:1.35;color:#444}

/* team */
.team{top:998px;height:839px;background:var(--grey-bg)}
.section-title{width:1200px;text-align:center;font-family:"Lato",sans-serif;font-weight:900;font-size:42px;color:var(--ink);letter-spacing:1px}
.section-title::after{content:"";display:block;width:130px;height:3px;background:var(--ink);margin:10px auto 0}
.team .section-title{top:74px}
.intro{left:200px;width:800px;text-align:center;font-size:12px;line-height:1.9;color:#555}
.team .intro{top:166px}
.tabs{left:113px;top:275px;width:970px;border-bottom:2px solid #333;height:37px;display:flex;gap:40px;font-family:"Lato",sans-serif;font-weight:700;font-size:15px;color:#333}
.tabs span{padding:4px 0}
.tabs .on{border-bottom:3px solid #333}
.member-photo{left:148px;top:365px;width:311px;height:310px;background:linear-gradient(160deg,#3b4a63,#7a8699 60%,#2a2f3a)}
.member-name{left:148px;width:311px;top:702px;text-align:center;font-family:"Lato",sans-serif;font-weight:700;font-size:17px;color:var(--ink)}
.member-role{left:148px;width:311px;top:733px;text-align:center;font-size:11px;color:#777}
.team-head{left:533px;top:402px;font-family:"Lato",sans-serif;font-weight:900;font-size:25px;color:var(--ink);letter-spacing:.5px}
.team-head::after{content:"";display:block;width:550px;height:1px;background:#bbb;margin-top:14px}
.team-bio{left:533px;top:468px;width:550px;font-size:12px;line-height:1.95;color:#555}
.btn-line{display:inline-block;border:1px solid #777;font-family:"Lato",sans-serif;font-weight:700;font-size:11px;letter-spacing:1.5px;color:#333;text-transform:uppercase;padding:13px 18px;border-radius:3px}
.team .slash{left:700px;top:716px;font-size:28px;color:#999}

/* testimonial */
.testimonial{top:1837px;height:563px;background:var(--white)}
.badge{left:246px;top:74px;width:110px;height:110px;border-radius:50%;background:#1b1b1b;border:5px solid var(--brand-red)}
.quote-title{left:380px;top:82px;font-family:"Lato",sans-serif;font-size:32px;color:var(--ink)}
.quote-by{left:380px;top:150px;font-family:"Lato",sans-serif;font-weight:700;font-size:11px;letter-spacing:1.8px;color:#333}
.quote-by::after{content:"";display:block;width:620px;height:1px;background:#ccc;margin-top:10px}
.quote-text{left:266px;top:208px;width:745px;font-size:15px;line-height:1.75;color:#444}
.dots{left:560px;top:454px;display:flex;gap:9px}
.dots i{width:11px;height:11px;border-radius:50%;background:#ccc;display:block}
.dots i.on{background:#333}

/* video */
.video{top:2400px;height:578px;background:linear-gradient(180deg,#0f2238,var(--gym-a) 40%,var(--gym-b))}
.video-kicker{width:1200px;top:170px;text-align:center;font-family:"Lato",sans-serif;font-weight:700;font-size:16px;letter-spacing:3px;color:var(--white)}
.video-title{width:1200px;top:232px;text-align:center;font-family:"Lato",sans-serif;font-weight:900;font-size:46px;letter-spacing:1px;color:var(--white)}
.video .btn-line{left:530px;top:326px;border-color:#fff;color:#fff;background:rgba(0,0,0,.2)}

/* contact */
.touch{top:2978px;height:370px;background:var(--white)}
.touch .section-title{top:70px}
.touch .intro{top:164px;left:180px;width:840px;font-size:13px}
.info-band{top:3348px;height:237px;background:linear-gradient(180deg,#2a2a2a,#5a2f2a 70%,#3b2b28)}
.info-col{top:55px;width:320px;color:var(--white)}
.info-col h4{font-family:"Lato",sans-serif;font-weight:900;font-size:24px;margin-bottom:12px;letter-spacing:.5px}
.info-col p{font-size:12px;line-height:1.7}
.form{top:3585px;height:533px;background:var(--white)}
.field{border:1px solid #ddd;background:#fafafa;height:44px;font-size:11px;color:#888;padding:14px 18px}
.form .btn-dark{left:113px;top:388px;font-size:11px;padding:14px 24px}

/* footer */
.site-footer{top:4118px;height:326px;background:var(--footer);color:#ccc}
.foot-col{top:55px}
.foot-col h5{font-family:"Lato",sans-serif;font-weight:700;font-size:17px;color:var(--white);margin-bottom:26px}
.foot-col ul{list-style:none;font-size:12px;line-height:2.6;color:#bbb}
.foot-col li::before{content:"›";margin-right:8px;color:#888}
.socials{display:flex;gap:26px}
.copyright{width:1200px;top:286px;text-align:center;font-size:11px;color:#999}
</style>
</head>
<body>

<header class="site-nav">
  <div class="brand abs">
    <div class="brand-name">MORVAL PASTIME</div>
    <div class="brand-tag">Health, Wellness, Fitness, Consultants</div>
  </div>
  <ul class="menu abs">
    <li>Home</li><li>Health</li><li>Wellness</li><li>Fitness</li><li>Brisk Rig</li><li>Our Team</li><li>Testimonials</li><li>Contact Us</li>
  </ul>
</header>

<section class="hero" role="img" aria-label="Dark-toned photograph of people training in a gym">
  <h1 class="hero-title abs">EXPERTS IN THE INDUSTRY</h1>
  <p class="hero-sub abs">WE ARE LEADING CONSULTANTS TO THE HEALTH, WELLNESS &amp; FITNESS INDUSTRY</p>
  <span class="btn-dark abs">Meet our team</span>
  <div class="polaroid abs" style="left:640px;top:60px;width:250px;height:240px;transform:rotate(-6deg)">
    <div role="img" aria-label="Photo of an athlete kicking outdoors" style="background:linear-gradient(160deg,#c9a77a,#6b8aa8)"></div>
  </div>
  <div class="polaroid abs" style="left:880px;top:75px;width:220px;height:220px;transform:rotate(7deg)">
    <div role="img" aria-label="Photo of a woman exercising" style="background:linear-gradient(160deg,#9bb8d6,#d9c6a8)"></div>
  </div>
  <div class="polaroid abs" style="left:820px;top:245px;width:250px;height:255px;transform:rotate(3deg)">
    <div role="img" aria-label="Photo of a smiling trainer" style="background:linear-gradient(160deg,#4f7a3d,#c9b49a)"></div>
  </div>
</section>

<section class="services">
  <div class="service abs" style="left:124px">
    <div class="icon" role="img" aria-label="Stethoscope photo" style="background:radial-gradient(circle,#e8f0f8,#6b9ac4)"></div>
    <h3>Health</h3>
    <p>Ut wisi enim ad minim veniam, quis nostrud exerci tation ullamcorper...</p>
  </div>
  <div class="service abs" style="left:458px">
    <div class="icon" role="img" aria-label="Spa stones and bamboo photo" style="background:radial-gradient(circle,#d8d4b0,#5b6b3a)"></div>
    <h3>Wellness</h3>
    <p>Ut wisi enim ad minim veniam, quis nostrud exerci tation ullamcorper...</p>
  </div>
  <div class="service abs" style="left:796px">
    <div class="icon" role="img" aria-label="Gym equipment photo" style="background:radial-gradient(circle,#e4e6ea,#7d8796)"></div>
    <h3>Fitness</h3>
    <p>Stet clita kasd gubergren, no sea takimata sanctus est... Sanctus...</p>
  </div>
</section>

<section class="team">
  <h2 class="section-title abs">OUR TEAM</h2>
  <p class="intro abs">Our team are certified professionals who will educate, motivate and keep you accountable. If you are new to exercise or having trouble staying fit, you need a personal trainer. Our goal is to get you exercising regularly and obtain results you want.</p>
  <div class="tabs abs"><span class="on">Alden Grove</span><span>Paul Corrin</span><span>Reid Elwood</span><span>Silas Wrenford</span></div>
  <div class="member-photo abs" role="img" aria-label="Portrait of the founder in a suit"></div>
  <div class="member-name abs">Alden Grove</div>
  <div class="member-role abs">Founder / Director</div>
  <h3 class="team-head abs">THE TEAM @ MORVAL PASTIME</h3>
  <p class="team-bio abs">Morval Pastime long term success depends on the talents commitment and shared values of our people. Morval Pastime is made of a unique hand picked team that will ensure the best possible service is delivered, as a company were passionate about delivering the best for our clients so we employ and partner with the best people who share that drive, passion and are led through the Morval values in everything they do. Our philosophy is based on open genuine collaborations working with organisations, who like us have a can do attitude proactive approach and who want to win, with over 25 years experience in the Health, Wellness and Fitness industry and many hundreds of happy clients we want to help build your business the right way!</p>
  <span class="btn-line abs" style="left:533px;top:713px">See team bio</span>
  <span class="slash abs">/</span>
  <span class="btn-line abs" style="left:735px;top:713px">Meet our team</span>
</section>

<section class="testimonial">
  <div class="badge abs" role="img" aria-label="Partner badge"></div>
  <h3 class="quote-title abs">"Highly Recommended"</h3>
  <div class="quote-by abs">JON DELANO - SUMMIT DASH CEO &amp; FOUNDER OF SUMMIT DASH</div>
  <p class="quote-text abs">Stridewell Summit Dash and Morval Pastime first collaborated in 2015. Alden and the Morval team have showed impeccable drive, commitment, passion and integrity throughout our partnership. With the help of the Morval team Summit Dash have gained huge success in the UK in 2015 and we are in great shape for 2016. Their ability to go to market quickly, professionally, with tenacity and high energy enables me to personally recommend the Morval Pastime organisation to anyone, or any company who requires a genuine, successful business collaboration and wants a great return on their investment "Highly Recommended"</p>
  <div class="dots abs"><i></i><i class="on"></i><i></i><i></i></div>
</section>

<section class="video" role="img" aria-label="Interior photograph of a modern gym floor with cardio machines">
  <div class="video-kicker abs">FEATURE VIDEO</div>
  <h2 class="video-title abs">BRISK RIG ELEVATE CIRCUIT</h2>
  <span class="btn-line abs">Watch now!</span>
</section>

<section class="touch">
  <h2 class="section-title abs">GET IN TOUCH</h2>
  <p class="intro abs">If you have any questions regarding gym facilities, services or schedules or have requests or suggestions to make, feel free to give us a call or fill out the form below. While members have access to our facility 24 hours daily, 365 days per year including holidays, guests may visit the club during our staffed hours for tours and information or to workout with a guest pass.</p>
</section>

<section class="info-band" role="img" aria-label="Dimmed photograph of a gymnasium entrance">
  <div class="info-col abs" style="left:113px">
    <h4>OUR LOCATION</h4>
    <p>Morval Pastime<br>The Larches<br>Ashvale<br>UK &amp; Ireland</p>
  </div>
  <div class="info-col abs" style="left:444px">
    <h4>CONTACT US</h4>
    <p>Phone:01632-960418 Office:01632-960772<br>Email: info@morvalpastime.com</p>
  </div>
  <div class="info-col abs" style="left:779px">
    <h4>STAFFED HOURS</h4>
    <p><strong>Monday to Friday 9-00am to 6-30pm Saturday 9-00am to 2-00pm</strong></p>
  </div>
</section>

<section class="form">
  <div class="field abs" style="left:113px;top:47px;width:470px">Name:</div>
  <div class="field abs" style="left:601px;top:47px;width:469px">Email:</div>
  <div class="field abs" style="left:113px;top:110px;width:470px">Phone:</div>
  <div class="field abs" style="left:601px;top:110px;width:469px">URL:</div>
  <div class="field abs" style="left:113px;top:175px;width:957px">Subject:</div>
  <div class="field abs" style="left:113px;top:237px;width:957px;height:128px">Message:</div>
  <span class="btn-dark abs">Send the message</span>
</section>

<footer class="site-footer">
  <div class="foot-col abs" style="left:190px">
    <h5>Find us online</h5>
    <div class="socials">
      <svg width="22" height="22" viewBox="0 0 22 22"><circle cx="11" cy="11" r="10" fill="#999"/></svg>
      <svg width="22" height="22" viewBox="0 0 22 22"><circle cx="11" cy="11" r="10" fill="#999"/></svg>
      <svg width="22" height="22" viewBox="0 0 22 22"><circle cx="11" cy="11" r="10" fill="#999"/></svg>
      <svg width="22" height="22" viewBox="0 0 22 22"><rect x="1" y="1" width="20" height="20" fill="#999"/></svg>
    </div>
  </div>
  <div class="foot-col abs" style="left:557px">
    <h5>Company</h5>
    <ul><li>About Us</li><li>Our Team</li><li>Testimonials</li><li>Contact Us</li></ul>
  </div>
  <div class="foot-col abs" style="left:880px">
    <h5>Features</h5>
    <ul><li>Health</li><li>Wellness</li><li>Fitness</li><li>Brisk Rig</li></ul>
  </div>
  <div class="copyright abs">Copyright © 2017 Morval Pastime</div>
</footer>

</body>
</html>
```